IT-support company web-site design

We need to re-design out site for existing clients and for the future promotions. Site needs to be attractive with intuitive interface. We need to keep our logo and colors but any reshuffles can be made. I provide the working site and re-made version, which we do nt like. It has to be more bright and clear. All the blocks have to be divided and look like logic and structured. PLease find the addresses to work with below.
The "real" one https://qorbil.com
The version http://tomuski.net/Qorbil/
If you have any с

Industry/Entity Type

It Company

Number of Pages Required

5+ page

Font styles to use
Sans Serif

Colors
9bcb3c

Requirements
Must have
• Our LOGO and our colors (green palette). We d like to make our services blocks as the main things. We need to have our images and slogans as there are extremely important advantages of our company.
Nice to have
• Original and modern view of the site.
Should not have
• unpredictable and @surprising@, hard- definable buttons and ways

```html
<!DOCTYPE html>
<html lang="en">
<head>
<meta charset="utf-8">
<title>Qorbil — IT Support</title>
<link href="https://fonts.googleapis.com/css2?family=Montserrat:wght@400;600;700;800&family=Open+Sans:wght@400;600&display=swap" rel="stylesheet">
<style>
:root{
  --green:#9bcb3c;
  --green-dark:#86b32c;
  --ink:#1e1e1e;
  --text:#6b6b6b;
  --light:#f2f2f2;
  --grey-box:#e8e8e8;
  --dark:#2a2b2d;
  --white:#ffffff;
}
*{margin:0;padding:0;box-sizing:border-box}
html,body{width:1200px;height:4119px;overflow:hidden}
body{font-family:"Open Sans",Arial,sans-serif;color:var(--text);background:var(--white);position:relative}
h1,h2,h3,h4,.mont{font-family:"Montserrat",Arial,sans-serif}
section,header,footer{position:absolute;left:0;width:1200px;overflow:hidden}
.abs{position:absolute}
.btn{position:absolute;display:flex;align-items:center;justify-content:center;border-radius:20px;font-family:"Montserrat",Arial,sans-serif;font-weight:700;font-size:9px;letter-spacing:.5px;text-transform:uppercase}
.btn-white{background:var(--white);color:var(--green)}
.btn-green{background:var(--green);color:var(--white)}
.btn-dark{background:#4a4a4a;color:var(--white)}

/* hero */
.hero{top:0;height:593px;background:linear-gradient(120deg,#2b2a27 0%,#3d3a33 40%,#5a5447 70%,#3a352d 100%)}
.hero-shade{position:absolute;inset:0;background:linear-gradient(90deg,rgba(0,0,0,.55),rgba(0,0,0,.15))}
.nav{position:absolute;top:44px;left:233px;width:734px;height:28px;display:flex;align-items:center;justify-content:space-between}
.brand{display:flex;align-items:center;gap:8px;color:var(--white);font-family:"Montserrat",sans-serif;font-size:22px;font-weight:400;letter-spacing:1px}
.brand-dot{width:14px;height:14px;border:2px solid var(--white);border-radius:50%}
.menu{display:flex;align-items:center;gap:26px;font-family:"Montserrat",sans-serif;font-size:10px;font-weight:700;color:var(--white);text-transform:uppercase}
.menu .cta{background:var(--green);padding:5px 12px;border-radius:14px}
.hero h1{position:absolute;left:233px;top:200px;font-size:42px;line-height:44px;font-weight:800;color:var(--white)}
.hero h1 .hl{color:var(--green)}
.hero .lead{position:absolute;left:233px;top:343px;width:520px;font-size:15px;line-height:22px;font-weight:600;color:var(--white)}

/* services */
.services{top:593px;height:472px;background:var(--white)}
.svc{position:absolute;width:220px;text-align:center}
.svc svg{display:block;margin:0 auto 10px}
.svc h3{font-size:12px;font-weight:700;color:var(--ink);line-height:15px;margin-bottom:8px}
.svc p{font-size:10px;line-height:13px}

/* invest */
.invest{top:1065px;height:454px;background:var(--green);color:var(--white)}
.invest h2{position:absolute;top:48px;left:0;width:1200px;text-align:center;font-size:20px;line-height:28px;font-weight:700}
.invest .sub{position:absolute;top:117px;left:300px;width:600px;text-align:center;font-size:10px;line-height:16px}
.offer{position:absolute;top:182px;width:234px}
.offer .ph{height:170px;border-radius:2px}
.offer h4{margin-top:16px;font-size:12px;font-weight:700}
.offer p{font-size:9px;margin-top:5px}

/* about / faq */
.about{top:1519px;height:403px}
.about h2{position:absolute;font-size:22px;font-weight:700;color:var(--ink)}
.about .txt{position:absolute;left:264px;width:340px;font-size:10px;line-height:14.6px}
.faq-item{position:absolute;left:643px;width:392px;height:48px;background:var(--grey-box);display:flex;align-items:center;padding-left:28px;font-size:10px;font-weight:600;color:var(--ink)}
.faq-item::before{content:"+";position:absolute;left:12px;font-weight:700}
.faq-open{position:absolute;left:643px;top:190px;width:392px}
.faq-open h4{font-family:"Open Sans",sans-serif;font-size:10px;font-weight:600;color:var(--green);padding-left:28px;position:relative}
.faq-open h4::before{content:"−";position:absolute;left:12px}
.faq-open p{font-size:9.5px;line-height:13px;padding-left:28px;margin-top:12px}

/* stats */
.stats{top:1922px;height:201px;background:var(--green);color:var(--white)}
.stat{position:absolute;top:68px;width:200px;text-align:center}
.stat b{display:block;font-family:"Montserrat",sans-serif;font-size:34px;font-weight:800;line-height:38px}
.stat span{font-size:11px;font-weight:600}

/* titles */
.sec-title{position:absolute;left:0;width:1200px;text-align:center}
.sec-title small{display:block;font-family:"Montserrat",sans-serif;font-size:8px;font-weight:700;letter-spacing:1.5px;color:var(--ink);text-transform:uppercase}
.sec-title h2{font-size:24px;font-weight:700;color:var(--ink);margin-top:8px}
.sec-title i{display:block;width:36px;height:3px;background:var(--green);margin:9px auto 0}

/* projects */
.projects{top:2123px;height:554px}
.tile{position:absolute;top:173px;width:276px;height:313px}

/* membership */
.membership{top:2677px;height:637px}
.plan{position:absolute;background:var(--white);border-radius:12px;box-shadow:0 4px 24px rgba(0,0,0,.1);text-align:center}
.plan h3{font-size:14px;font-weight:800;color:var(--ink);margin-top:50px}
.plan .kind{font-size:8px}
.plan .price{font-size:12px;color:var(--ink);margin-top:16px}
.plan .price sup{font-size:8px}
.plan .price b{font-size:20px;font-weight:700}
.plan ul{list-style:none;margin-top:26px}
.plan li{font-size:9px;height:31px;line-height:31px;border-bottom:1px solid #eee;margin:0 30px}
.plan.best{background:var(--green);color:var(--white)}
.plan.best h3,.plan.best .price{color:var(--white)}
.plan.best li{border-color:rgba(255,255,255,.3)}

/* contact */
.contact{top:3314px;height:470px;background:var(--green);color:var(--white)}
.contact h2{position:absolute;left:233px;top:50px;font-size:16px;line-height:22px;font-weight:700}
.team{position:absolute;left:233px;top:127px;width:316px;height:134px;display:grid;grid-template-columns:repeat(4,1fr);gap:5px}
.team div{background:linear-gradient(160deg,#b4906c,#5f4a3b)}
.contact .txt{position:absolute;left:233px;top:291px;width:330px;font-size:9px;line-height:12px}
.form{position:absolute;left:607px;top:58px;width:360px;height:352px;background:var(--light);border-radius:4px}
.form h3{text-align:center;margin-top:57px;font-size:16px;font-weight:700;color:var(--ink)}
.field{position:absolute;background:var(--white);border-radius:12px;font-size:8px;color:#777;padding:0 12px;display:flex;align-items:center}

/* footer */
.footer{top:3784px;height:335px;background:var(--dark);color:var(--white);text-align:center}
.footer small{position:absolute;top:48px;left:0;width:1200px;font-family:"Montserrat",sans-serif;font-size:8px;font-weight:700;letter-spacing:1px}
.footer h2{position:absolute;top:62px;left:0;width:1200px;font-size:17px;line-height:22px;font-weight:700;color:var(--green)}
.footer .txt{position:absolute;top:112px;left:350px;width:500px;font-size:9px;line-height:14px}
.sub-form{position:absolute;left:376px;top:170px;width:437px;height:34px;display:flex}
.sub-form span{flex:1;background:var(--white);color:#555;font-size:10px;display:flex;align-items:center;padding-left:14px}
.sub-form b{width:118px;background:var(--green);font-family:"Montserrat",sans-serif;font-size:9px;display:flex;align-items:center;justify-content:center;text-transform:uppercase}
.copy{position:absolute;top:288px;left:0;width:1200px;font-size:8px;color:#999}
.social{position:absolute;top:300px;left:0;width:1200px;display:flex;justify-content:center;gap:8px}
.social i{width:9px;height:9px;border-radius:50%;background:#aaa}
</style>
</head>
<body>

<header class="hero">
  <div class="abs" style="inset:0" role="img" aria-label="Photo of a team working together at laptops"></div>
  <div class="hero-shade"></div>
  <nav class="nav">
    <div class="brand"><span class="brand-dot"></span>QORBIL</div>
    <div class="menu"><span>Home</span><span>About</span><span>Services</span><span>Personal</span><span>Banking</span><span class="cta">Contact Us</span></div>
  </nav>
  <h1>We Make Your<br><span class="hl">Information Technology</span><br>SECURE and SIMPLE</h1>
  <p class="lead">Lorem ipsum dolor sit amet, consectetur adipiscing elit, sed do eiusmod tempor incididunt ut labore et dolore magna aliqua. Ut enim ad minim.</p>
  <a class="btn btn-white" style="left:233px;top:415px;width:124px;height:26px">Read More</a>
</header>

<section class="services">
  <div class="svc" style="left:247px;top:88px">
    <svg width="28" height="28" viewBox="0 0 28 28" fill="none" stroke="#9bcb3c" stroke-width="2"><rect x="5" y="3" width="18" height="22" rx="2"/><path d="M10 11h8M10 16h8"/></svg>
    <h3>Travel and Aviation<br>Consulting</h3>
    <p>Lorem ipsum dolor sit amet, consectetur , do eiusmod tempor incididunt ut labore et dolore magna aliqua.</p>
  </div>
  <div class="svc" style="left:491px;top:88px">
    <svg width="28" height="28" viewBox="0 0 28 28" fill="none" stroke="#9bcb3c" stroke-width="2"><circle cx="14" cy="14" r="6"/><circle cx="14" cy="14" r="11"/></svg>
    <h3>Business Services<br>Consulting</h3>
    <p>Lorem ipsum dolor sit amet, consectetur , do eiusmod tempor incididunt ut labore et dolore magna aliqua.</p>
  </div>
  <div class="svc" style="left:736px;top:88px">
    <svg width="28" height="28" viewBox="0 0 28 28" fill="none" stroke="#9bcb3c" stroke-width="2"><rect x="4" y="4" width="20" height="20" rx="2"/><path d="M8 18l5-5 3 3 4-5"/></svg>
    <h3>Beginner - friendly<br>admin options</h3>
    <p>Lorem ipsum dolor sit amet, consectetur , do eiusmod tempor incididunt ut labore et dolore magna aliqua.</p>
  </div>
  <div class="svc" style="left:247px;top:266px">
    <svg width="28" height="28" viewBox="0 0 28 28" fill="none" stroke="#9bcb3c" stroke-width="2"><path d="M5 10h18v14H5zM9 10V6h10v4"/></svg>
    <h3>Consumer Products<br>Consulting</h3>
    <p>Lorem ipsum dolor sit amet, consectetur , do eiusmod tempor incididunt ut labore et dolore magna aliqua.</p>
  </div>
  <div class="svc" style="left:491px;top:266px">
    <svg width="28" height="28" viewBox="0 0 28 28" fill="none" stroke="#9bcb3c" stroke-width="2"><circle cx="14" cy="14" r="10"/><path d="M14 8v6l4 3"/></svg>
    <h3>Surface Transport &amp;<br>Logistics Consulting</h3>
    <p>Lorem ipsum dolor sit amet, consectetur , do eiusmod tempor incididunt ut labore et dolore magna aliqua.</p>
  </div>
  <div class="svc" style="left:736px;top:266px">
    <svg width="28" height="28" viewBox="0 0 28 28" fill="none" stroke="#9bcb3c" stroke-width="2"><rect x="4" y="7" width="20" height="15" rx="2"/><path d="M4 12h20"/></svg>
    <h3>Financial Services<br>Consulting</h3>
    <p>Lorem ipsum dolor sit amet, consectetur , do eiusmod tempor incididunt ut labore et dolore magna aliqua.</p>
  </div>
</section>

<section class="invest">
  <h2>Invest in Our Company And Have Healthy<br>Profits Long Treams</h2>
  <p class="sub">Lorem ipsum dolor sit amet, consectetur , do eiusmod tempor incididunt ut labore et dolore magna aliqua. Lorem ipsum dolor sit amet, consectetur , do eiusmod tempor incididunt ut labore et dolore magna aliqua.</p>
  <div class="offer" style="left:233px"><div class="ph" role="img" aria-label="Photo of a woman working at a desk" style="background:linear-gradient(150deg,#e4ddd2,#a88e74)"></div><h4>Financial Support</h4><p>Provide Business Financial Support</p></div>
  <div class="offer" style="left:483px"><div class="ph" role="img" aria-label="Photo of a business advisor in a suit" style="background:linear-gradient(150deg,#a89580,#4e3e31)"></div><h4>Business Advisor</h4><p>Provide Business Financial Support</p></div>
  <div class="offer" style="left:733px"><div class="ph" role="img" aria-label="Photo of a man presenting at a whiteboard" style="background:linear-gradient(150deg,#eae8e4,#b39476)"></div><h4>Loan Programs</h4><p>Provide Business Financial Support</p></div>
</section>

<section class="about">
  <h2 style="left:264px;top:56px">About us</h2>
  <h2 style="left:643px;top:56px">Frequently Asked Question</h2>
  <p class="txt" style="top:118px">Lorem ipsum dolor sit amet, consectetur adipiscing elit, sed do eiusmod tempor incididunt ut labore et dolore magna aliqua. Ut enim ad minim veniam, quis nostrud exercitation ullamco laboris nisi ut aliquip ex ea commodo consequat. Duis aute irure dolor in reprehenderit in voluptate velit esse cillum dolore eu fugiat nulla pariatur.</p>
  <p class="txt" style="top:229px">Lorem ipsum dolor sit amet, consectetur adipiscing elit, sed do eiusmod tempor incididunt ut labore et dolore magna aliqua. Ut enim ad minim veniam, quis nostrud exercitation ullamco.</p>
  <a class="btn btn-green" style="left:264px;top:312px;width:107px;height:26px">More About</a>
  <div class="faq-item" style="top:120px">How can I Get Help by Company</div>
  <div class="faq-open"><h4>What about Loan Programs &amp; Advantage?</h4><p>Lorem Ipsum is simply dummy text of the printing and typesetting industry. Lorem Ipsum has been the industry's standard dummy text ever since the 1500s, when an unknown.</p></div>
  <div class="faq-item" style="top:293px;height:44px">What about Invest Plan &amp; Process</div>
</section>

<section class="stats">
  <div class="stat" style="left:139px"><b>84</b><span>Satisfied Client</span></div>
  <div class="stat" style="left:383px"><b>758</b><span>Completed Projects</span></div>
  <div class="stat" style="left:622px"><b>125</b><span>Team Member</span></div>
  <div class="stat" style="left:850px"><b>12+</b><span>Years Experience</span></div>
</section>

<section class="projects">
  <div class="sec-title" style="top:78px"><small>What We Created</small><h2>Our best projects</h2><i></i></div>
  <div class="tile" role="img" aria-label="Project: pink helmet filled with candy" style="left:19px;background:linear-gradient(160deg,#f27aa8,#e94c8c)"></div>
  <div class="tile" role="img" aria-label="Project: two smart watches on blue" style="left:310px;background:linear-gradient(160deg,#2ea6f5,#1689e0)"></div>
  <div class="tile" role="img" aria-label="Project: business cards on pink and orange" style="left:603px;background:linear-gradient(160deg,#f2a9c8 0%,#f2a9c8 50%,#f58a4a 50%,#f27d3c 100%)"></div>
  <div class="tile" role="img" aria-label="Project: illustrated drink bottle on mint" style="left:900px;width:281px;background:linear-gradient(160deg,#bfe7e4,#9fd8d6)"></div>
</section>

<section class="membership">
  <div class="sec-title" style="top:53px"><small>What We Showcased</small><h2>MemberShip</h2><i></i></div>
  <div class="plan" style="left:283px;top:151px;width:178px;height:371px">
    <h3>BASIC PLAN</h3><div class="kind">Standard Pricing Plan</div>
    <div class="price"><sup>$</sup><b>35</b>/ monthly</div>
    <ul><li>Free Clients Support</li><li>Easy Implementation</li><li>Great Private Policy</li><li>Top Result Guarantee</li></ul>
    <a class="btn btn-dark" style="left:54px;top:306px;width:70px;height:22px">Read More</a>
  </div>
  <div class="plan best" style="left:486px;top:135px;width:192px;height:406px">
    <h3 style="margin-top:58px">THE BEST PLAN</h3><div class="kind">Standard Pricing Plan</div>
    <div class="price"><sup>$</sup><b>35</b>/ monthly</div>
    <ul><li>Free Clients Support</li><li>Easy Implementation</li><li>Great Private Policy</li><li>Top Result Guarantee</li></ul>
    <a class="btn btn-white" style="left:61px;top:322px;width:70px;height:22px">Read More</a>
  </div>
  <div class="plan" style="left:700px;top:151px;width:187px;height:371px">
    <h3>BASIC PLAN</h3><div class="kind">Standard Pricing Plan</div>
    <div class="price"><sup>$</sup><b>35</b>/ monthly</div>
    <ul><li>Free Clients Support</li><li>Easy Implementation</li><li>Great Private Policy</li><li>Top Result Guarantee</li></ul>
    <a class="btn btn-dark" style="left:58px;top:306px;width:70px;height:22px">Read More</a>
  </div>
</section>

<section class="contact">
  <h2>Feel Free to Get in<br>Touch With us Any Convenient way</h2>
  <div class="team" role="img" aria-label="Grid of eight team member portraits"><div></div><div></div><div></div><div></div><div></div><div></div><div></div><div></div></div>
  <p class="txt">At dictum molestie mattis. Vivamus hendrerit, justo a sollicitudin ultricies, tellus sem rutrum sapien, id volutpat justo orci non mi. Aenean malesuada justo quis lectus, sit amet efficitur arcu laoreet.</p>
  <a class="btn btn-white" style="left:233px;top:365px;width:91px;height:26px">Submit</a>
  <div class="form">
    <h3>Contact with us</h3>
    <div class="field" style="left:27px;top:116px;width:148px;height:22px">Yourname</div>
    <div class="field" style="left:187px;top:116px;width:146px;height:22px">you@mail.com</div>
    <div class="field" style="left:27px;top:150px;width:306px;height:22px">Subject</div>
    <div class="field" style="left:27px;top:184px;width:306px;height:63px;align-items:flex-start;padding-top:7px;border-radius:10px">Message</div>
    <a class="btn btn-green" style="left:123px;top:284px;width:114px;height:26px">Send Message</a>
  </div>
</section>

<footer class="footer">
  <small>GET IN TOUCH WITH OUR NEWS</small>
  <h2>Sign up to our ns<br>and be the first to know all the news</h2>
  <p class="txt">Vestibulum nec cursus nibh. Donec ultrices ornare tincidunt. Nunc lacus ante, fermentum vel pretium non, egestas sed odio.</p>
  <div class="sub-form"><span>Type your email</span><b>Subscribe</b></div>
  <p class="copy">© 2018 QORBIL All Rights Reserved</p>
  <div class="social"><i></i><i></i><i></i><i></i></div>
</footer>

</body>
</html>
```